Detailing informational flyer

I want to design a new flyer for my automotive detailing business. The flyer should use the color scheme from the logo and be easy to read and understand the services we offer.

Font styles to use
Serif
Sans Serif

Colors
3176b5
0255a3
fbed22
33a6d7
0692cd
ffffff

Requirements
Must have
• must include all information from the copy
Nice to have
• include a Glenvaro logo such as the image attached

```html
<!DOCTYPE html>
<html lang="en">
<head>
<meta charset="utf-8">
<title>Rapid Lube &amp; Detailing Center – Service Flyer</title>
<link rel="stylesheet" href="https://fonts.googleapis.com/css2?family=Oswald:wght@500;600;700&family=PT+Sans:wght@400&display=swap">
<style>
  :root{
    --yellow:#fbed22;
    --navy:#0255a3;
    --mid-blue:#3176b5;
    --sky:#33a6d7;
    --cyan:#0692cd;
    --white:#ffffff;
    --paper-top:#cfe0ee;
    --paper-bottom:#eef4f9;
    --ink:#1a1a1a;
    --backdrop:#e6e6e6;
    --brand-ink:#14285a;
  }
  *{margin:0;padding:0;box-sizing:border-box;}
  html,body{width:1200px;height:825px;overflow:hidden;background:var(--backdrop);}
  .canvas{position:relative;width:1200px;height:825px;}
  .page{position:absolute;top:90px;width:467px;height:640px;overflow:hidden;background:linear-gradient(180deg,var(--paper-top),var(--paper-bottom));}
  .page--front{left:101px;}
  .page--back{left:634px;}
  .page__art{position:absolute;inset:0;width:100%;height:100%;}

  .title{position:absolute;left:10px;top:4px;font-family:"Oswald",sans-serif;font-weight:700;font-size:62px;line-height:66px;color:var(--yellow);text-shadow:0 2px 4px rgba(0,0,0,.35);}

  .brand{position:absolute;left:300px;top:362px;width:160px;text-align:center;font-family:"Oswald",sans-serif;font-weight:600;font-size:16px;line-height:20px;letter-spacing:1.5px;color:var(--brand-ink);}

  .section{position:absolute;left:11px;right:11px;text-align:center;}
  .section__heading{font-family:"Oswald",sans-serif;font-weight:600;font-size:18.5px;line-height:22px;color:var(--navy);}
  .section__body{font-family:"PT Sans",sans-serif;font-size:13px;line-height:15px;color:var(--ink);text-align:justify;text-align-last:center;}
  .section__body--center{text-align:center;}

  .front-intro{top:465px;}
  .front-exterior{top:514px;}
  .back-interior{top:8px;}
  .back-mini{top:109px;}
  .back-headlight{top:239px;}

  .footer{position:absolute;left:0;right:0;bottom:0;height:34px;display:flex;align-items:center;justify-content:center;gap:16px;background:var(--navy);font-family:"Oswald",sans-serif;font-weight:500;font-size:14.5px;color:var(--yellow);}
  .footer__address{color:#f3ec8a;}
  .footer__divider{color:var(--white);}
  .footer__phone{font-weight:600;font-size:15.5px;}
</style>
</head>
<body>
<main class="canvas">

  <section class="page page--front">
    <svg class="page__art" viewBox="0 0 584 800" preserveAspectRatio="none">
      <defs>
        <linearGradient id="washPhoto" x1="0" y1="0" x2="0.4" y2="1">
          <stop offset="0" stop-color="#5f6f80"/>
          <stop offset="0.5" stop-color="#9aa4ae"/>
          <stop offset="1" stop-color="#2c3440"/>
        </linearGradient>
      </defs>
      <g role="img" aria-label="Photo of a car covered in foam inside an automatic car wash">
        <polygon points="0,0 584,0 584,305 0,590" fill="url(#washPhoto)"/>
      </g>
      <polygon points="174,507 584,300 584,587" fill="var(--sky)"/>
      <polygon points="0,580 584,298 584,310 0,596" fill="var(--yellow)"/>
      <polygon points="170,502 584,582 584,594 178,514" fill="var(--yellow)"/>
    </svg>

    <h1 class="title">Rapid Lube &amp;<br>Detailing Center</h1>

    <p class="brand">BROOKMERE<br>DETAIL CENTER</p>

    <div class="section front-intro">
      <h2 class="section__heading">Brookmere Carwash Detailing Center:</h2>
      <p class="section__body section__body--center">Ask to speak to a manager about scheduling any of our detailing services.</p>
    </div>

    <div class="section front-exterior">
      <h2 class="section__heading">Exterior detailing includes</h2>
      <p class="section__body">We wash, clay, compound, polish, and wax, as needed to restore the deep rich gloss and provide a durable shine for that “new car” look. This process removes light oxidation from the vehicle and protects the clear coat finish. Finishing touches include rim cleaning and tire shine.</p>
    </div>

    <footer class="footer">
      <span class="footer__address">48-20 Linden Parkway Ashford Heights 10492</span>
      <span class="footer__divider">|</span>
      <span class="footer__phone">+1 555-014-2280</span>
    </footer>
  </section>

  <section class="page page--back">
    <svg class="page__art" viewBox="0 0 584 800" preserveAspectRatio="none">
      <defs>
        <linearGradient id="tunnelPhoto" x1="0" y1="0" x2="0" y2="1">
          <stop offset="0" stop-color="#0c2a3a"/>
          <stop offset="0.55" stop-color="#2f6f86"/>
          <stop offset="1" stop-color="#0a2230"/>
        </linearGradient>
      </defs>
      <g role="img" aria-label="Photo of a windshield with water streaks inside a car wash tunnel">
        <polygon points="0,387 308,455 584,520 584,800 0,800" fill="url(#tunnelPhoto)"/>
      </g>
      <polygon points="308,455 584,386 584,520" fill="var(--navy)"/>
      <polygon points="0,383 308,451 308,457 0,389" fill="var(--yellow)"/>
      <polygon points="304,452 584,382 584,392 312,458" fill="var(--yellow)"/>
      <polygon points="304,452 584,514 584,526 312,460" fill="var(--yellow)"/>
    </svg>

    <div class="section back-interior">
      <h2 class="section__heading">Interior detailing shampoo includes</h2>
      <p class="section__body">We perform a deep cleaning of the interior such as the dashboard, door jams, center console, trunk area, upholstered seats, and all carpets and mats. This process will remove soils and most stains. Windows are cleaned inside and out. All leather is dressed to provide a protective finish. Air fresher is available upon request.</p>
    </div>

    <div class="section back-mini">
      <h2 class="section__heading">Mini detail/ VIP service includes</h2>
      <p class="section__body">Brookmere Special Wash with triple polish wax, Glenvaro Shield protectant, tire shine, and a detailed and gentle cleaning of the upholstery. 4 rubber or carpet mats are shampooed. All interior surfaces are dressed including dash-board, door panels, center console. This is followed by a detailed carpet and upholstery vacuum with compressed air to remove dirt from hard to reach places. For added shine ask about adding on our express wax service to your mini detail package.</p>
    </div>

    <div class="section back-headlight">
      <h2 class="section__heading">Headlight restoration</h2>
      <p class="section__body">This shop proudly offers the Headlight Service, which can polish or restore your headlight to a clear, safe condition at a fraction of the cost of headlight replacement! Restore the lens to a clear, shiny &amp; safe condition.</p>
    </div>

    <footer class="footer">
      <span class="footer__address">48-20 Linden Parkway Ashford Heights 10492</span>
      <span class="footer__divider">|</span>
      <span class="footer__phone">+1 555-014-2280</span>
    </footer>
  </section>

</main>
</body>
</html>
```